TRI FOLD BROCHURE

I need a trifold brochure designed for my carpet cleaning company. It will be specifically for realtors and real estate attorneys. I have the text content I need in the brochure available as well as the company logo and a spotted dog picture we use in most of our marketing.

Industry/Entity Type

Real Estate

```html
<!DOCTYPE html>
<html lang="en">
<head>
<meta charset="utf-8">
<title>Pristine Floor Care – Tri-fold Brochure</title>
<link href="https://fonts.googleapis.com/css2?family=Oswald:wght@600;700&family=Montserrat:wght@700;800&family=Open+Sans:wght@400;600;700&display=swap" rel="stylesheet">
<style>
:root{
  --stage:#2e2e2e;
  --blue:#3a8fc9;
  --blue-deep:#1f6ea8;
  --blue-light:#5aa9dc;
  --panel:#f1f2f3;
  --panel-edge:#e2e4e6;
  --ink:#4a4a4a;
  --white:#ffffff;
  --room:linear-gradient(180deg,#f6f6f6 0%,#e4e4e4 30%,#d2d2d2 48%,#eeeeee 62%,#f8f8f8 78%,#d6d6d6 100%);
  --wood:linear-gradient(180deg,#d9d2c4 0%,#c7bba6 34%,#9a6a3a 40%,#7a4a22 70%,#5a3314 100%);
  --sofa:linear-gradient(180deg,#e2dfdb 0%,#cfc9c3 22%,#9b7a76 30%,#7d5e5c 70%,#5f4544 100%);
  --family:linear-gradient(180deg,#eceef0 0%,#d8c8b6 35%,#b98f6c 60%,#2d3348 85%,#22283a 100%);
}
*{margin:0;padding:0;box-sizing:border-box}
html,body{width:1200px;height:887px;overflow:hidden;background:var(--stage)}
body{position:relative;font-family:"Open Sans",Arial,sans-serif;color:var(--ink)}
.sheet{position:absolute;overflow:hidden}
.photo{position:absolute}
.photo-room{background:var(--room)}
.photo-wood{background:var(--wood)}
.photo-sofa{background:var(--sofa)}
.photo-family{background:var(--family)}
.wave{position:absolute;left:0;width:100%}
.brand{position:absolute;font-family:"Montserrat",sans-serif;font-weight:800;color:var(--white);text-transform:uppercase;line-height:1.05;text-align:center}
.seal{position:absolute;border-radius:50%;background:var(--blue-deep);border:3px solid var(--white)}
.headline{position:absolute;font-family:"Oswald",sans-serif;font-weight:700;color:var(--white);text-transform:uppercase;line-height:1.02;text-align:center}
.contact{position:absolute;color:var(--white);font-size:8px;line-height:1.3}
.contact .cta{font-weight:700;font-size:9px}
.contact .phone{font-family:"Oswald",sans-serif;font-weight:700;font-size:20px;letter-spacing:.5px;line-height:1.1;border-bottom:1.5px solid var(--white);display:inline-block;margin-bottom:3px}
.web{position:absolute;color:var(--white);font-size:8px;letter-spacing:1.4px}
.section-title{font-family:"Montserrat",sans-serif;font-weight:800;color:var(--blue);text-transform:uppercase;font-size:11px;line-height:1.25}
.bullets{list-style:none;font-size:7px;line-height:1.35}
.bullets li{position:relative;padding-left:7px;margin-bottom:6px}
.bullets li::before{content:"";position:absolute;left:0;top:3px;width:4px;height:4px;border-radius:50%;background:currentColor}
.bullets.tight{line-height:1.22}
.bullets.tight li{margin-bottom:0}

/* outside spread */
.outside{left:35px;top:10px;width:543px;height:418px;background:var(--blue)}
.outside .flap{position:absolute;left:0;top:0;width:178px;height:100%;background:linear-gradient(90deg,var(--white),var(--panel))}
.outside .flap .section-title{position:absolute;left:12px;top:91px}
.outside .flap .bullets{position:absolute;left:12px;top:112px;width:156px}
.outside .tagline{position:absolute;left:12px;top:342px;width:165px;font-family:"Oswald",sans-serif;font-weight:700;font-size:12.5px;line-height:1.25;color:var(--white);text-shadow:1px 1px 0 #555,0 0 3px #555;text-transform:uppercase}
.outside .cover{position:absolute;left:178px;top:0;width:365px;height:100%;background:linear-gradient(180deg,var(--blue) 0%,var(--blue-deep) 100%)}

/* inside spread */
.inside{left:55px;top:443px;width:545px;height:419px;background:var(--panel)}
.inside .band-top{position:absolute;left:0;top:0;width:100%;height:36px;background:var(--blue)}
.inside .band-bottom{position:absolute;left:0;bottom:0;width:100%;height:48px;background:linear-gradient(180deg,var(--blue-light) 0 6px,var(--blue) 6px 10px,var(--blue-deep) 10px)}
.inside .fold{position:absolute;top:0;width:1px;height:100%;background:var(--panel-edge)}
.inside .col{position:absolute}
.inside .rounded{border-radius:8px;border:2px solid var(--white);box-shadow:0 1px 4px rgba(0,0,0,.25)}
.note-box{position:absolute;left:192px;top:207px;width:165px;height:66px;border-radius:8px;background:var(--blue);color:var(--white);padding:7px 6px 0 8px}
.note-box .bullets{font-size:6.6px}

/* cover cards */
.card{background:var(--blue)}
.card-front{left:634px;top:220px;width:233px;height:642px}
.card-rack{left:922px;top:125px;width:235px;height:537px;background:linear-gradient(180deg,var(--blue-light),var(--blue))}
.card-rack-back{left:897px;top:138px;width:30px;height:530px;background:var(--blue)}
</style>
</head>
<body>

<!-- Outside spread -->
<section class="sheet outside">
  <div class="flap">
    <h2 class="section-title">Our Cleaning Agents</h2>
    <ul class="bullets">
      <li>Are only the safest GREEN cleaning agents available, so there are never any health concerns for babies or pets.</li>
      <li>Are able to destroy over 600 known pathogens, viruses, bacteria, funguses and microbial so they cannot regrow</li>
      <li>Are advanced encapsulation products that do not leave any soil attracting residue behind which keep your floors and furniture looking brighter and newer longer.</li>
      <li>Utilize a fraction of the the water of other cleaning methods. One room requires about 1/2 gallon of water unlike roughly 10 gallons with steam cleaning. This allows it to dry in about 1 HOUR!</li>
    </ul>
    <p class="tagline">Nothing but faster, safer,<br>and better floor care!</p>
  </div>
  <div class="cover">
    <div class="photo photo-room" style="left:0;top:118px;width:365px;height:180px" role="img" aria-label="Row of spotted puppies sitting on a spotted white carpet in a bright living room with white sofas"></div>
    <svg class="wave" style="top:270px" width="365" height="40" viewBox="0 0 365 40" aria-hidden="true"><path d="M0 14 C90 34 220 -4 365 22 L365 40 L0 40Z" fill="#2b7fbb"/><path d="M0 18 C90 38 220 0 365 26" stroke="#8cc6ec" stroke-width="2" fill="none"/></svg>
    <div class="brand" style="left:200px;top:26px;width:160px;font-size:19px">Pristine<br><span style="font-size:10px;letter-spacing:1px">Floor Care</span></div>
    <div class="seal" style="left:239px;top:76px;width:76px;height:76px"></div>
    <div class="contact" style="left:14px;top:341px">
      <div class="cta">Free Estimates - Give Us A Call Today</div>
      <div class="phone">877-555-0142</div>
      <div>Pristine Floor Care Lexington<br>482 Maple Ln<br>Lexington KY 40502</div>
    </div>
    <div class="headline" style="left:196px;top:312px;width:160px;font-size:17.5px">Do your floor or upholstery have you seeing spots?</div>
    <div class="web" style="left:213px;top:396px">www.pristinefloorcare.com</div>
  </div>
</section>

<!-- Inside spread -->
<section class="sheet inside">
  <div class="band-top"></div>
  <div class="fold" style="left:181px"></div>
  <div class="fold" style="left:363px"></div>
  <div class="web" style="left:372px;top:38px;color:var(--blue)">www.pristinefloorcare.com</div>

  <div class="col" style="left:0;top:94px;width:175px">
    <div class="photo photo-family" style="position:relative;width:175px;height:100px" role="img" aria-label="Smiling couple on a sofa with their two dogs"></div>
    <h2 class="section-title" style="margin:14px 0 0 12px">Reasons Homeowners<br>Love Pristine<br>Floor Care</h2>
    <p style="margin:5px 0 0 12px;font-size:7px;line-height:1.35;width:158px">No cleaning method can promise 100% removal of contaminates in your carpet. However, our proprietary cleaning system has been repeatedly tested and proven to produce results that are at least 25% cleaner than even the most powerful steam cleaning systems available</p>
  </div>

  <div class="col" style="left:195px;top:92px;width:162px">
    <h2 class="section-title">Our Equipment</h2>
    <ul class="bullets tight" style="margin-top:3px">
      <li>Is amazingly fast. It has won multiple national competitions for a combination of speed and thoroughness. Most households can be cleaned in under 2 hours!</li>
      <li>Uses the most technologically advanced equipment in the industry</li>
      <li>Utilizes a patented hyper agitation pattern that Harlow Mills has deemed to be safe for and non damaging to the carpet</li>
      <li>Does NOT utilize hoses that</li>
    </ul>
  </div>
  <div class="note-box">
    <ul class="bullets tight">
      <li>cause damage to floors, door jams &amp; walls</li>
      <li>require doors to stay open causing risk of pets of children escaping as well as weather concerns</li>
      <li>limit cleaning access to higher areas or long distances from parking access</li>
    </ul>
  </div>

  <div class="photo photo-wood rounded" style="left:382px;top:80px;width:144px;height:113px" role="img" aria-label="Technician cleaning a polished wooden floor in an empty room"></div>
  <div class="photo photo-sofa rounded" style="left:382px;top:202px;width:144px;height:111px" role="img" aria-label="Patterned sofa being cleaned with an upholstery tool"></div>

  <div class="band-bottom"></div>
  <div class="contact" style="left:373px;top:377px">
    <div class="cta">Free Estimates - Give Us A Call Today</div>
    <div class="phone" style="border:none">877-555-0142</div>
  </div>
</section>

<!-- Front cover card -->
<section class="sheet card card-front">
  <div style="position:absolute;left:0;top:0;width:100%;height:134px;background:linear-gradient(180deg,var(--blue-light),var(--blue))"></div>
  <div class="photo photo-room" style="left:0;top:152px;width:233px;height:222px" role="img" aria-label="Spotted puppies sitting in front of white spotted sofas"></div>
  <svg class="wave" style="top:350px" width="233" height="50" viewBox="0 0 233 50" aria-hidden="true"><path d="M0 16 C60 40 150 -2 233 24 L233 50 L0 50Z" fill="#2b7fbb"/><path d="M0 20 C60 44 150 2 233 28" stroke="#8cc6ec" stroke-width="2" fill="none"/></svg>
  <div style="position:absolute;left:0;top:398px;width:100%;height:244px;background:var(--blue-deep)"></div>
  <div class="contact" style="left:17px;top:440px">
    <div class="cta">Free Estimates - Give Us A Call Today</div>
    <div class="phone">877-555-0142</div>
    <div>Pristine Floor Care Lexington<br>482 Maple Ln<br>Lexington KY 40502</div>
  </div>
</section>

<!-- Rack cover card -->
<div class="sheet card card-rack-back"></div>
<section class="sheet card card-rack">
  <div class="brand" style="left:15px;top:28px;width:205px;font-size:26px">Pristine<br><span style="font-size:12px;letter-spacing:1.5px">Floor Care</span></div>
  <div class="seal" style="left:75px;top:92px;width:84px;height:84px"></div>
  <div class="photo photo-room" style="left:0;top:156px;width:235px;height:222px" role="img" aria-label="Spotted puppies on a spotted carpet beside white sofas"></div>
  <svg class="wave" style="top:352px" width="235" height="46" viewBox="0 0 235 46" aria-hidden="true"><path d="M0 16 C60 40 150 -2 235 24 L235 46 L0 46Z" fill="#2b7fbb"/><path d="M0 20 C60 44 150 2 235 28" stroke="#8cc6ec" stroke-width="2" fill="none"/></svg>
  <div style="position:absolute;left:0;top:396px;width:100%;height:141px;background:var(--blue-deep)"></div>
  <div class="headline" style="left:12px;top:402px;width:211px;font-size:24px">Do your floor or<br>upholstery have<br>you seeing spots?</div>
  <div class="web" style="left:42px;top:506px">www.pristinefloorcare.com</div>
</section>

</body>
</html>
```